Business Card design project for new family-run construction business

We need a logo and business card designed for a new construction company. We want to convey a professional, but approachable image. We hope to be servicing small residential clients as well as large commercial contracts as well.
Our business will employ a single "Hydro excavator" truck, which can be used for multiple purposes: vacuuming up dirt or water, digging holes, clearing sewer blockages and so on.
We are open to different colour schemes, however blue and white, or yellow/green would be good combinations. We are open to multiple colours (2-4), so long as they are complimentary.

EDIT: Let's not put much emphasis on the octopus... unless it's very clear that the arms are actual vacuum hoses, it won't make sense. An octopus on it's own has little to do with our business.

Please also do not use actual photos of hydro-vac trucks. This is not the aesthetic we are going for.

**The logo should instead be: A stylized outline of a hydrovac truck (a line drawing or digital version of a line-drawing). See the two examples in the attached images of hydrovac trucks. I've also included a very crude pen outline as a reference. Please use your artistic discretion and talent (as I clearly have none) to make something that looks much nicer. Thanks for your efforts!**

The front of the card should have the following elements:
Logo
Name: P & K Hydro Excavation and Flushign
Two phone numbers: Direct and Office
Email address
Website
It should also have the name of the employee and their job title
At the bottom of the card it should say (in a noticeable way): "24/7 Emergency Calls Welcome"

The back of the card should have the following elements:
"20 Years Experience"
"A Canadian Family Run Business"
A small maple-leaf logo that is in a similar style to the rest of the card/logos in the bottom right corner of the back of the card. (see attached)

**We have just added a number of business card designs that really appeal to us to offer inspiration.**

Reason: We have not received designs that hit the mark of what we are looking for. Feedback has been posted, so we would like to provide the designers more time.

Target Market(s)

Commercial and residential customers. As big as large malls and office buildings, as small single-family home owners

Industry/Entity Type

Construction Company

Contact Information for Business Card

We have just added a number of business card designs that really appeal to us to offer inspiration.

Logo
Email address
Website

"20 Years Experience"

Logo Text

P & K Hydro Excavation and Flushing

Font styles to use
Serif
Sans Serif
Other font styles liked:
• Helvetica, Futura, Impact, bold strong, modern fonts that convey a sense of design and style

Colors
0592cd
ec1f27
9bcb3c

Requirements
Must have
• The front of the card should have the following elements:
• Logo
• Name: P & K Hydro Excavation and Flushign
• Two phone numbers: Direct and Office
• Email address
• Website
• It should also have the name of the employee and their job title
• At the bottom of the card it should say (in a noticeable way): "24/7 Emergency Calls Welcome"
• The back of the card should have the following elements:
• "20 Years Experience"
• "A Canadian Family Run Business"
• A small maple-leaf logo that is in a similar style to the rest of the card/logos in the bottom right corner of the back of the card. (see attached)
Nice to have
• The card does not have to be a perfect rectangle. We are open to rounded corners or cut out elements.
• Also embossing, engraving, adding highlighted/glossy layers (spot glass?), or any other effect that will give the card a unique look/feel is more than welcome.
• We would love to have a card that stands out from others and is compelling to look at it, so we are happy to incorporate any sort of modern printing technology to bring out the design.
• Please feel encouraged to be creative and design something unique, especially for this industry.
• Our dream would be if a Scandinavian architect were to go into the construction business and design this business card ;)
Should not have
• Photographs

```html
<!DOCTYPE html>
<html lang="en">
<head>
<meta charset="utf-8">
<title>P & K Hydro Excavation and Flushign — Business Card</title>
<link rel="stylesheet" href="https://fonts.googleapis.com/css2?family=Exo+2:ital,wght@0,300;0,400;1,300;1,400&display=swap">
<style>
  :root {
    --ink: #1e1e1d;
    --paper: #ffffff;
    --edge: #a6a6a6;
    --gold: #a3875f;
    --silver: #bdbbba;
    --copper: #9f6e50;
    --copper-light: #c9a286;
    --text-dark: #1a1a1a;
  }
  html, body {
    margin: 0;
    padding: 0;
    width: 1009px;
    height: 1200px;
    overflow: hidden;
    background: var(--paper);
  }
  .canvas {
    position: relative;
    width: 1009px;
    height: 1200px;
    font-family: "Exo 2", sans-serif;
  }
  .shapes {
    position: absolute;
    inset: 0;
  }
  .text {
    position: absolute;
    margin: 0;
    white-space: nowrap;
    line-height: 1;
  }
  .tagline {
    left: 266px;
    width: 600px;
    text-align: center;
    color: var(--gold);
    font-style: italic;
    font-weight: 300;
    font-size: 39px;
  }
  .tagline--years { top: 215px; }
  .tagline--family { top: 264px; }

  .brand {
    position: absolute;
    display: flex;
    align-items: center;
    gap: 12px;
  }
  .brand__mark {
    width: 22px;
    height: 22px;
    border-radius: 50%;
    flex: none;
  }
  .brand__name {
    font-weight: 400;
    font-size: 22px;
    line-height: 1.05;
    white-space: nowrap;
  }
  .brand--back { left: 40px; top: 470px; }
  .brand--back .brand__mark { background: var(--silver); }
  .brand--back .brand__name { color: var(--silver); }
  .brand--front { left: 68px; top: 720px; }
  .brand--front .brand__mark { background: var(--copper); }
  .brand--front .brand__name { color: var(--copper); font-size: 24px; }

  .contact {
    right: 580px;
    text-align: right;
    color: var(--text-dark);
    font-style: italic;
    font-weight: 300;
    font-size: 26px;
  }
  .contact--phone { top: 967px; }
  .contact--street { top: 1019px; right: 609px; }
  .contact--city { top: 1052px; right: 602px; }

  .person {
    left: 596px;
    width: 290px;
    text-align: center;
    color: var(--paper);
    font-style: italic;
  }
  .person__name { top: 942px; font-weight: 300; font-size: 46px; }
  .person__title { top: 996px; font-weight: 300; font-size: 25px; }
  .emergency {
    left: 520px;
    width: 440px;
    text-align: center;
    color: var(--paper);
    font-style: italic;
    font-weight: 300;
    font-size: 28px;
    top: 1127px;
  }
</style>
</head>
<body>
<div class="canvas">
  <svg class="shapes" width="1009" height="1200" viewBox="0 0 1009 1200" aria-hidden="true">
    <defs>
      <linearGradient id="tab-fill" x1="0" y1="0" x2="1" y2="0">
        <stop offset="0" stop-color="#9a684a"/>
        <stop offset="0.6" stop-color="#b3866a"/>
        <stop offset="1" stop-color="#d7bca8"/>
      </linearGradient>
    </defs>

    <!-- back side -->
    <polygon class="back-card" points="345,1 998,1 998,573 1,573 1,360"
             fill="var(--ink)" stroke="var(--edge)" stroke-width="2"/>

    <!-- front side -->
    <rect class="front-card" x="12" y="623" width="996" height="572"
          fill="var(--paper)" stroke="var(--edge)" stroke-width="1"/>
    <rect class="front-rule" x="57" y="814" width="334" height="4" fill="var(--ink)"/>

    <g class="contact-tabs">
      <polygon points="458,921 560,921 560,999 438,999 438,941" fill="url(#tab-fill)"/>
      <polygon points="435,1002 540,1002 540,1077 415,1077 415,1022" fill="url(#tab-fill)"/>
      <polygon points="411,1080 520,1080 520,1157 391,1157 391,1100" fill="url(#tab-fill)"/>
    </g>

    <polygon class="front-panel" points="667,623 1009,980 1009,1195 454,1195" fill="var(--ink)"/>

    <g class="icon-phone">
      <circle cx="490" cy="958" r="19" fill="var(--paper)"/>
      <path d="M482,948 l5,-2 l3,7 l-3,3 q2,5 7,8 l3,-3 l7,3 l-2,5 q-10,2 -17,-7 q-6,-8 -3,-14 z" fill="var(--ink)"/>
    </g>
    <g class="icon-pin">
      <path d="M461,1052 q-15,-18 -15,-27 a15,15 0 0 1 30,0 q0,9 -15,27 z" fill="var(--paper)"/>
      <circle cx="461" cy="1025" r="7" fill="var(--ink)"/>
    </g>
    <g class="icon-mail">
      <rect x="414" y="1104" width="50" height="34" rx="5" fill="var(--paper)" stroke="#000" stroke-width="4"/>
      <path d="M416,1107 L439,1125 L462,1107" fill="none" stroke="#000" stroke-width="4" stroke-linejoin="round"/>
    </g>
  </svg>

  <p class="text tagline tagline--years">20 Years Experience</p>
  <p class="text tagline tagline--family">A Canadian Family Run Business</p>

  <div class="brand brand--back">
    <span class="brand__mark"></span>
    <span class="brand__name">P &amp; K<br>Hydro Excavation<br>and Flushign</span>
  </div>

  <div class="brand brand--front">
    <span class="brand__mark"></span>
    <span class="brand__name">P &amp; K<br>Hydro Excavation<br>and Flushign</span>
  </div>

  <p class="text contact contact--phone">555 014 2290 / 555 014 2290</p>
  <p class="text contact contact--street">218 Birchwood Avenue Newton,</p>
  <p class="text contact contact--city">NY 10482</p>

  <p class="text person person__name">Marco lenes</p>
  <p class="text person person__title">President</p>
  <p class="text emergency">24/7 Emergency Calls Welcome</p>
</div>
</body>
</html>
```